Tovalmer's 50th Anniversary Gala

Need a cool invitation to be printed on #120 paper for a nonprofit gala fundraiser. Verbiage for invitation is below. Event logo is attached. Could potentially use black and gold but NOT a requirement. Want it to be FUN and DIFFERENT.

Colors
0054AA
0677BA
7BADD7
CADEEF
E8F1F8

```html
<!DOCTYPE html>
<html lang="en">
<head>
<meta charset="utf-8">
<title>Tovalmer's 50th Anniversary Gala – Invitation</title>
<link rel="stylesheet" href="https://fonts.googleapis.com/css2?family=Great+Vibes&family=Montserrat:wght@400;500;700&display=swap">
<style>
  :root {
    --page-bg: #e9eaec;
    --card-bg: #0b0c0e;
    --card-bg-soft: #17191b;
    --gold: #e6cd86;
    --gold-deep: #b98d45;
    --gold-light: #f3df92;
    --rule: #c9a85a;
  }
  * { margin: 0; padding: 0; box-sizing: border-box; }
  html, body {
    width: 1200px;
    height: 1200px;
    overflow: hidden;
    background: var(--page-bg);
  }
  .invitation {
    position: absolute;
    left: 205px;
    top: 55px;
    width: 790px;
    height: 1090px;
    background: radial-gradient(ellipse at 55% 45%, var(--card-bg-soft) 0%, var(--card-bg) 65%);
    color: var(--gold);
    font-family: "Montserrat", sans-serif;
    overflow: hidden;
  }
  .line {
    position: absolute;
    left: 0;
    width: 100%;
    text-align: center;
    line-height: 1;
    white-space: nowrap;
  }
  .invite-lead { top: 94px; font-size: 24px; }
  .event-mark {
    position: absolute;
    top: 176px;
    left: 0;
    width: 100%;
    display: flex;
    justify-content: center;
    align-items: center;
    gap: 14px;
  }
  .event-mark__dot {
    width: 22px;
    height: 22px;
    border-radius: 50%;
    background: var(--gold);
  }
  .event-mark__name {
    font-size: 50px;
    font-weight: 500;
    color: var(--gold);
    line-height: 1;
  }
  .event-title {
    top: 250px;
    padding: 14px 0 26px;
    font-family: "Great Vibes", cursive;
    font-weight: 400;
    font-size: 124px;
    line-height: 1.4;
    background: linear-gradient(90deg, var(--gold-deep), var(--gold-light) 45%, var(--gold-deep) 75%, var(--gold-light));
    -webkit-background-clip: text;
    background-clip: text;
    color: transparent;
    overflow: visible;
  }
  .date-rule {
    position: absolute;
    left: 267px;
    width: 262px;
    height: 2px;
    background: var(--rule);
  }
  .date-rule--top { top: 441px; }
  .date-rule--bottom { top: 508px; }
  .event-date { top: 458px; font-size: 31px; font-weight: 700; color: #f1dc9a; }
  .event-date sup { font-size: 17px; vertical-align: 14px; }
  .event-time { top: 533px; font-size: 24px; }
  .venue-name { top: 606px; font-size: 24px; }
  .venue-address { top: 648px; font-size: 24px; }
  .refreshments {
    position: absolute;
    top: 706px;
    left: 0;
    width: 100%;
    display: flex;
    justify-content: center;
    align-items: center;
    gap: 42px;
    font-size: 24px;
    line-height: 1;
  }
  .refreshments svg { width: 26px; height: 26px; fill: var(--gold); }
  .dress-code { top: 767px; font-size: 24px; }
  .chevron-band {
    position: absolute;
    left: 0;
    top: 842px;
    width: 100%;
    height: 96px;
    background: linear-gradient(90deg, var(--gold-deep), var(--gold-light) 30%, var(--gold-deep) 65%, var(--gold-light));
    opacity: 0.9;
  }
  .ticket-note { top: 982px; font-size: 20px; }
</style>
</head>
<body>
  <main class="invitation">
    <p class="line invite-lead">Join us for a memorable night!</p>

    <div class="event-mark">
      <span class="event-mark__dot"></span>
      <span class="event-mark__name">Tovalmer</span>
    </div>

    <h1 class="line event-title">Gala Celebration</h1>

    <div class="date-rule date-rule--top"></div>
    <p class="line event-date">Friday, November 8<sup>th</sup></p>
    <div class="date-rule date-rule--bottom"></div>

    <p class="line event-time">6:30 – 10 p.m.</p>
    <p class="line venue-name">The Marlowe</p>
    <p class="line venue-address">2416 Larkspur Avenue</p>

    <div class="refreshments">
      <svg viewBox="0 0 24 24" aria-hidden="true"><polygon points="12,1 15,9 23.5,9 16.7,14.2 19.3,22.5 12,17.4 4.7,22.5 7.3,14.2 0.5,9 9,9"/></svg>
      <span>Hors d’oeuvres and Cocktails</span>
      <svg viewBox="0 0 24 24" aria-hidden="true"><polygon points="12,1 15,9 23.5,9 16.7,14.2 19.3,22.5 12,17.4 4.7,22.5 7.3,14.2 0.5,9 9,9"/></svg>
    </div>

    <p class="line dress-code">Semi-formal</p>

    <div class="chevron-band" role="img" aria-label="Gold zigzag chevron pattern band"></div>

    <p class="line ticket-note">Ticket information on reverse</p>
  </main>
</body>
</html>
```